Flyer for American Indian Elders on Dementia Warning Signs

We need a flyer designed for older adults who are American Indian or Alaska Native (in the U.S.).

Ideally, the flyer should complement the colors of our logos. The project logo and our organization logo are attached to the brief.

When people see the flyer we want them to feel that it represents their culture, is warm, and professional but relatable to older adults and people who have limited incomes.

I have attached an earlier draft of the document we designed ourselves BUT we want different and better.

It is for older adults who have trouble reading so:
1. you must use a font that is 11.5 points or larger
2. Do not put text over complex pictures or use shading with words
3. You can use a serif font for the heading, but should use san serif for the body text
4. There should be good contrast between the font color and background

Please do not use any images that include a head dress or pictures of American Indian people or things that are very traditional or "token" imagery.

We need to save a small space under the call out box/ somewhere on the flyer for other people to add their logo once they download.

Let us know if you have questions or need additional information.

Target Market(s)

Older American Indian people

Font styles to use
Serif
Sans Serif

Requirements
Must have
• Easy to read for older adults
Should not have
• indian headdress

```html
<!DOCTYPE html>
<html lang="en">
<head>
<meta charset="utf-8">
<title>10 Signs of Thinking or Memory Changes – Flyer Versions</title>
<link href="https://fonts.googleapis.com/css2?family=Poppins:wght@400;500;600;700;800&display=swap" rel="stylesheet">
<style>
:root{
  --maroon:#a0443f;
  --maroon-deep:#3e1616;
  --teal-dark:#1f5a5f;
  --teal:#3f9da0;
  --grey-band:#e6e6e6;
  --grey-box:#ededed;
  --ink:#2b2b2b;
  --white:#ffffff;
}
*{box-sizing:border-box;margin:0;padding:0}
html,body{width:1200px;height:4000px;overflow:hidden;background:var(--white)}
body{position:relative;font-family:"Poppins",Arial,sans-serif;color:var(--ink)}
.sheet{position:absolute;left:200px;width:790px;height:1120px;background:var(--white);box-shadow:0 4px 14px rgba(0,0,0,.28)}
.version-label{position:absolute;left:0;width:1200px;text-align:center;font-weight:600;font-size:40px;color:#222}
.version-label span{display:inline-block;padding:0 14px 6px;border-bottom:3px solid #eee}
.masthead{position:absolute;left:0;top:0;width:100%;height:115px;background:var(--grey-band)}
.org{position:absolute;left:34px;top:30px;width:130px;display:flex;flex-direction:column;align-items:center;gap:8px}
.org-mark{width:40px;height:40px;background:var(--teal)}
.org-name{font-size:9px;font-weight:600;color:var(--maroon);text-align:center;line-height:1.15;text-transform:uppercase}
.badge{position:absolute;left:174px;top:32px;width:72px;height:68px;background:var(--maroon);color:var(--white);text-align:center}
.badge-num{font-size:46px;font-weight:800;line-height:48px;display:block}
.badge-word{font-size:12px;font-weight:700;letter-spacing:1px;display:block;line-height:14px}
.title{position:absolute;left:256px;top:30px;text-transform:uppercase;font-weight:800;line-height:1}
.title-top{display:block;font-size:24px;color:var(--teal-dark);letter-spacing:-.3px}
.title-main{display:block;font-size:32px;color:var(--teal-dark);letter-spacing:-.6px;margin-top:4px}
.intro{position:absolute;left:35px;top:131px;width:720px;height:140px;background:var(--teal-dark);color:var(--white);padding:12px 20px;font-size:12px;line-height:1.3}
.intro p{width:480px;margin-bottom:9px}
.intro strong{font-weight:700}
.intro-photo{position:absolute;left:520px;top:14px;width:178px;height:112px}
.prompt{position:absolute;left:35px;top:290px;font-size:20px;font-weight:700;color:var(--maroon);letter-spacing:-.2px}
.signs{position:absolute;left:35px;top:326px;width:412px;height:694px;list-style:none;display:flex;flex-direction:column;justify-content:space-between}
.sign{display:flex;gap:10px}
.sign-num{flex:0 0 32px;height:32px;border-radius:50%;background:var(--maroon);color:var(--white);font-size:13px;font-weight:700;display:flex;align-items:center;justify-content:center;margin-top:2px}
.sign-text{font-size:11.5px;line-height:1.25}
.sign-head{font-weight:700;color:var(--teal-dark);font-size:12.5px}
.sign-lead{color:var(--teal)}
.sign-text ul{list-style:none;padding-left:14px}
.sign-text li{position:relative}
.sign-text li::before{content:"";position:absolute;left:-11px;top:5px;width:5px;height:5px;border:1px solid var(--maroon);border-radius:50%}
.facts{position:absolute;left:462px;top:320px;width:293px;height:460px;border-radius:14px;overflow:hidden;background:var(--maroon-deep);display:flex;flex-direction:column}
.fact{flex:1;display:flex}
.fact-icon{flex:0 0 78px;display:flex;align-items:center;justify-content:center;background:var(--teal-dark)}
.fact:nth-child(even) .fact-icon{background:var(--teal)}
.fact-text{flex:1;display:flex;align-items:center;padding:0 14px;color:var(--white);font-size:13px;line-height:1.3;border-bottom:1px solid rgba(255,255,255,.15)}
.fact:last-child .fact-text{border-bottom:0;font-weight:700}
.hub{position:absolute;left:468px;top:820px;width:290px;height:80px;display:flex;align-items:center;gap:12px}
.hub-mark{flex:0 0 70px;height:70px;border-radius:50%;border:3px solid var(--teal)}
.hub-name{font-size:17px;font-weight:600;color:var(--teal);line-height:1.15;text-transform:uppercase}
.visit{position:absolute;left:462px;top:916px;width:293px}
.visit-bar{height:36px;background:var(--teal-dark);color:var(--white);font-size:14px;display:flex;align-items:center;padding-left:74px}
.visit-links{display:flex;height:58px;background:var(--teal)}
.visit-icon{flex:0 0 50px;background:var(--maroon);display:flex;align-items:center;justify-content:center}
.visit-urls{flex:1;display:flex;flex-direction:column;justify-content:center;align-items:center;color:var(--white);font-weight:600;font-size:13px;line-height:1.35}
.partner-space{position:absolute;left:462px;top:1024px;width:293px;height:56px;background:var(--grey-box)}
.funding{position:absolute;left:35px;top:1035px;width:360px;font-size:7px;line-height:1.3;color:#444}
</style>
</head>
<body>

<!-- Version 1 -->
<section class="sheet" style="top:123px">
  <div class="masthead">
    <div class="org"><span class="org-mark"></span><span class="org-name">Elder Circle Alliance</span></div>
    <div class="badge"><span class="badge-num">10</span><span class="badge-word">SIGNS</span></div>
    <h1 class="title"><span class="title-top">of thinking or memory changes</span><span class="title-main">that might be dementia</span></h1>
  </div>
  <div class="intro">
    <p>As we get older, we may slow down a bit.</p>
    <p>This is a normal part of aging. Changes in memory or thinking that make it harder to get through the day, are <u>not</u> a normal part of aging. <strong>These may be early signs of dementia.</strong></p>
    <p>Because American Indian and Alaska Native people have a high risk of dementia, it is important to know the warning signs.</p>
    <div class="intro-photo" role="img" aria-label="Photo of an elder and a young girl sitting together outdoors" style="background:linear-gradient(180deg,#6f93b8 0%,#9fb4c6 45%,#c49a72 100%)"></div>
  </div>
  <h2 class="prompt">Do you have any of these 10 signs? If so, talk to your doctor.</h2>
  <ol class="signs">
    <li class="sign"><span class="sign-num">01</span><div class="sign-text"><span class="sign-head">Memory loss that affects your daily life.</span> <span class="sign-lead">You may:</span><ul><li>Forget events or important dates</li><li>Repeat yourself</li><li>Rely more often on lists or sticky notes to remember things</li></ul></div></li>
    <li class="sign"><span class="sign-num">02</span><div class="sign-text"><span class="sign-head">Trouble planning or solving problems.</span> <span class="sign-lead">You may have a harder time:</span><ul><li>Paying bills</li><li>Cooking recipes you have used for years</li></ul></div></li>
    <li class="sign"><span class="sign-num">03</span><div class="sign-text"><span class="sign-head">Get confused about the time, date, or where you are.</span></div></li>
    <li class="sign"><span class="sign-num">04</span><div class="sign-text"><span class="sign-head">Daily tasks are getting harder, including:</span><ul><li>Driving</li><li>Making a grocery list or going shopping</li></ul></div></li>
    <li class="sign"><span class="sign-num">05</span><div class="sign-text"><span class="sign-head">Trouble with how your eyesight and thinking work together that gets worse.</span> <span class="sign-lead">This includes:</span><ul><li>Tripping, falls, or problems with your balance</li><li>Spilling or dropping things more</li></ul></div></li>
    <li class="sign"><span class="sign-num">06</span><div class="sign-text"><span class="sign-head">New trouble talking or writing.</span><br>You may have a harder time finding the words you want to say. For example, you may say “that thing on your wrist that tells time” instead of “watch.”</div></li>
    <li class="sign"><span class="sign-num">07</span><div class="sign-text"><span class="sign-head">Lose and cannot find things.</span> <span class="sign-lead">For example, you:</span><ul><li>Can't find the coffee pot that you use every day</li><li>Might put your car keys in the freezer</li></ul></div></li>
    <li class="sign"><span class="sign-num">08</span><div class="sign-text"><span class="sign-head">Notice changes in mood or personality,</span> <span class="sign-lead">such as being:</span><ul><li>Easily mad or sad in everyday situations</li><li>More fearful (scared) or suspicious (not trusting)</li></ul></div></li>
    <li class="sign"><span class="sign-num">09</span><div class="sign-text"><span class="sign-head">Act different and make poor choices.</span> <span class="sign-lead">You may:</span><ul><li>Spend money you do not have or be a scam victim</li><li>Stop washing up regularly or pay less attention to how you look</li><li>Forget to take care of your pet</li></ul></div></li>
    <li class="sign"><span class="sign-num">10</span><div class="sign-text"><span class="sign-head">Pull away from friends and family because it is harder to keep up.</span><br>You may not want to do things you used to enjoy, like sporting events, church, music, or sex.</div></li>
  </ol>
  <aside class="facts">
    <div class="fact"><div class="fact-icon"><svg width="46" height="46" viewBox="0 0 46 46" fill="none" stroke="#fff" stroke-width="2"><path d="M23 6c-6 0-10 4-10 9s4 8 10 8 10-3 10-8-4-9-10-9z"/><path d="M23 6v17M16 12h4M26 16h4"/><path d="M6 22l6 14h8M40 22l-6 14h-8"/></svg></div><div class="fact-text">American Indian and Alaska Native people have a high risk of dementia.</div></div>
    <div class="fact"><div class="fact-icon"><svg width="46" height="46" viewBox="0 0 46 46" fill="none" stroke="#fff" stroke-width="2"><circle cx="20" cy="9" r="4"/><path d="M20 14v14l-4 12M20 28l5 12M14 20l6-4 6 6"/><path d="M32 22v18"/></svg></div><div class="fact-text">Big changes in memory or thinking that make it hard to get through the day are not a normal part of aging.</div></div>
    <div class="fact"><div class="fact-icon"><svg width="46" height="46" viewBox="0 0 46 46" fill="none" stroke="#fff" stroke-width="2"><circle cx="23" cy="13" r="7"/><path d="M9 40c0-9 6-14 14-14s14 5 14 14z"/><path d="M17 28v6a3 3 0 006 0"/></svg></div><div class="fact-text">People with one or more of these 10 signs should talk to their doctor to find the cause. It is not always dementia.</div></div>
    <div class="fact"><div class="fact-icon"><svg width="46" height="46" viewBox="0 0 46 46" fill="none" stroke="#fff" stroke-width="2"><rect x="9" y="8" width="24" height="32" rx="2"/><rect x="16" y="5" width="10" height="6"/><path d="M21 15v8M17 19h8M14 28h14M14 33h10"/><circle cx="34" cy="34" r="6"/><path d="M31 34l2 2 4-4"/></svg></div><div class="fact-text">Early dementia diagnosis gives you a chance to get care and plan your future.</div></div>
  </aside>
  <div class="hub"><span class="hub-mark"></span><span class="hub-name">Native Elders Brain Wellness Hub</span></div>
  <div class="visit">
    <div class="visit-bar">To learn more, visit:</div>
    <div class="visit-links"><span class="visit-icon"><svg width="20" height="20" viewBox="0 0 20 20" fill="none" stroke="#fff" stroke-width="1.6"><circle cx="10" cy="10" r="8"/><path d="M2 10h16M10 2c3 3 3 13 0 16M10 2c-3 3-3 13 0 16"/></svg></span><span class="visit-urls"><span>www.elderbrainwellness.org</span><span>www.healthyagingnet.org</span></span></div>
  </div>
  <div class="partner-space"></div>
  <p class="funding">This flyer is supported by a public health grant from a federal agency as part of an award for elder brain health outreach. The contents are those of the authors and do not represent official views of, nor an endorsement by, any agency.</p>
</section>
<p class="version-label" style="top:1272px"><span>Version 1</span></p>

<!-- Version 2 -->
<section class="sheet" style="top:1395px">
  <div class="masthead">
    <div class="org"><span class="org-mark"></span><span class="org-name">Elder Circle Alliance</span></div>
    <div class="badge"><span class="badge-num">10</span><span class="badge-word">SIGNS</span></div>
    <h1 class="title"><span class="title-top">of thinking or memory changes</span><span class="title-main">that might be dementia</span></h1>
  </div>
  <div class="intro">
    <p>As we get older, we may slow down a bit.</p>
    <p>This is a normal part of aging. Changes in memory or thinking that make it harder to get through the day, are <u>not</u> a normal part of aging. <strong>These may be early signs of dementia.</strong></p>
    <p>Because American Indian and Alaska Native people have a high risk of dementia, it is important to know the warning signs.</p>
    <div class="intro-photo" role="img" aria-label="Photo of a smiling elder woman in a pink top sitting outdoors" style="background:linear-gradient(135deg,#a88566 0%,#c9a27f 50%,#d36aa0 100%)"></div>
  </div>
  <h2 class="prompt">Do you have any of these 10 signs? If so, talk to your doctor.</h2>
  <ol class="signs">
    <li class="sign"><span class="sign-num">01</span><div class="sign-text"><span class="sign-head">Memory loss that affects your daily life.</span> <span class="sign-lead">You may:</span><ul><li>Forget events or important dates</li><li>Repeat yourself</li><li>Rely more often on lists or sticky notes to remember things</li></ul></div></li>
    <li class="sign"><span class="sign-num">02</span><div class="sign-text"><span class="sign-head">Trouble planning or solving problems.</span> <span class="sign-lead">You may have a harder time:</span><ul><li>Paying bills</li><li>Cooking recipes you have used for years</li></ul></div></li>
    <li class="sign"><span class="sign-num">03</span><div class="sign-text"><span class="sign-head">Get confused about the time, date, or where you are.</span></div></li>
    <li class="sign"><span class="sign-num">04</span><div class="sign-text"><span class="sign-head">Daily tasks are getting harder, including:</span><ul><li>Driving</li><li>Making a grocery list or going shopping</li></ul></div></li>
    <li class="sign"><span class="sign-num">05</span><div class="sign-text"><span class="sign-head">Trouble with how your eyesight and thinking work together that gets worse.</span> <span class="sign-lead">This includes:</span><ul><li>Tripping, falls, or problems with your balance</li><li>Spilling or dropping things more</li></ul></div></li>
    <li class="sign"><span class="sign-num">06</span><div class="sign-text"><span class="sign-head">New trouble talking or writing.</span><br>You may have a harder time finding the words you want to say. For example, you may say “that thing on your wrist that tells time” instead of “watch.”</div></li>
    <li class="sign"><span class="sign-num">07</span><div class="sign-text"><span class="sign-head">Lose and cannot find things.</span> <span class="sign-lead">For example, you:</span><ul><li>Can't find the coffee pot that you use every day</li><li>Might put your car keys in the freezer</li></ul></div></li>
    <li class="sign"><span class="sign-num">08</span><div class="sign-text"><span class="sign-head">Notice changes in mood or personality,</span> <span class="sign-lead">such as being:</span><ul><li>Easily mad or sad in everyday situations</li><li>More fearful (scared) or suspicious (not trusting)</li></ul></div></li>
    <li class="sign"><span class="sign-num">09</span><div class="sign-text"><span class="sign-head">Act different and make poor choices.</span> <span class="sign-lead">You may:</span><ul><li>Spend money you do not have or be a scam victim</li><li>Stop washing up regularly or pay less attention to how you look</li><li>Forget to take care of your pet</li></ul></div></li>
    <li class="sign"><span class="sign-num">10</span><div class="sign-text"><span class="sign-head">Pull away from friends and family because it is harder to keep up.</span><br>You may not want to do things you used to enjoy, like sporting events, church, music, or sex.</div></li>
  </ol>
  <aside class="facts">
    <div class="fact"><div class="fact-icon"><svg width="46" height="46" viewBox="0 0 46 46" fill="none" stroke="#fff" stroke-width="2"><path d="M23 6c-6 0-10 4-10 9s4 8 10 8 10-3 10-8-4-9-10-9z"/><path d="M23 6v17M16 12h4M26 16h4"/><path d="M6 22l6 14h8M40 22l-6 14h-8"/></svg></div><div class="fact-text">American Indian and Alaska Native people have a high risk of dementia.</div></div>
    <div class="fact"><div class="fact-icon"><svg width="46" height="46" viewBox="0 0 46 46" fill="none" stroke="#fff" stroke-width="2"><circle cx="20" cy="9" r="4"/><path d="M20 14v14l-4 12M20 28l5 12M14 20l6-4 6 6"/><path d="M32 22v18"/></svg></div><div class="fact-text">Big changes in memory or thinking that make it hard to get through the day are not a normal part of aging.</div></div>
    <div class="fact"><div class="fact-icon"><svg width="46" height="46" viewBox="0 0 46 46" fill="none" stroke="#fff" stroke-width="2"><circle cx="23" cy="13" r="7"/><path d="M9 40c0-9 6-14 14-14s14 5 14 14z"/><path d="M17 28v6a3 3 0 006 0"/></svg></div><div class="fact-text">People with one or more of these 10 signs should talk to their doctor to find the cause. It is not always dementia.</div></div>
    <div class="fact"><div class="fact-icon"><svg width="46" height="46" viewBox="0 0 46 46" fill="none" stroke="#fff" stroke-width="2"><rect x="9" y="8" width="24" height="32" rx="2"/><rect x="16" y="5" width="10" height="6"/><path d="M21 15v8M17 19h8M14 28h14M14 33h10"/><circle cx="34" cy="34" r="6"/><path d="M31 34l2 2 4-4"/></svg></div><div class="fact-text">Early dementia diagnosis gives you a chance to get care and plan your future.</div></div>
  </aside>
  <div class="hub"><span class="hub-mark"></span><span class="hub-name">Native Elders Brain Wellness Hub</span></div>
  <div class="visit">
    <div class="visit-bar">To learn more, visit:</div>
    <div class="visit-links"><span class="visit-icon"><svg width="20" height="20" viewBox="0 0 20 20" fill="none" stroke="#fff" stroke-width="1.6"><circle cx="10" cy="10" r="8"/><path d="M2 10h16M10 2c3 3 3 13 0 16M10 2c-3 3-3 13 0 16"/></svg></span><span class="visit-urls"><span>www.elderbrainwellness.org</span><span>www.healthyagingnet.org</span></span></div>
  </div>
  <div class="partner-space"></div>
  <p class="funding">This flyer is supported by a public health grant from a federal agency as part of an award for elder brain health outreach. The contents are those of the authors and do not represent official views of, nor an endorsement by, any agency.</p>
</section>
<p class="version-label" style="top:2564px"><span>Version2</span></p>

<!-- Version 3 -->
<section class="sheet" style="top:2640px">
  <div class="masthead">
    <div class="org"><span class="org-mark"></span><span class="org-name">Elder Circle Alliance</span></div>
    <div class="badge"><span class="badge-num">10</span><span class="badge-word">SIGNS</span></div>
    <h1 class="title"><span class="title-top">of thinking or memory changes</span><span class="title-main">that might be dementia</span></h1>
  </div>
  <div class="intro">
    <p>As we get older, we may slow down a bit.</p>
    <p>This is a normal part of aging. Changes in memory or thinking that make it harder to get through the day, are <u>not</u> a normal part of aging. <strong>These may be early signs of dementia.</strong></p>
    <p>Because American Indian and Alaska Native people have a high risk of dementia, it is important to know the warning signs.</p>
    <div class="intro-photo" role="img" aria-label="Photo of an elder man in a hat standing by a brick wall" style="background:linear-gradient(135deg,#9a6a50 0%,#7a5240 50%,#3a2a22 100%)"></div>
  </div>
  <h2 class="prompt">Do you have any of these 10 signs? If so, talk to your doctor.</h2>
  <ol class="signs">
    <li class="sign"><span class="sign-num">01</span><div class="sign-text"><span class="sign-head">Memory loss that affects your daily life.</span> <span class="sign-lead">You may:</span><ul><li>Forget events or important dates</li><li>Repeat yourself</li><li>Rely more often on lists or sticky notes to remember things</li></ul></div></li>
    <li class="sign"><span class="sign-num">02</span><div class="sign-text"><span class="sign-head">Trouble planning or solving problems.</span> <span class="sign-lead">You may have a harder time:</span><ul><li>Paying bills</li><li>Cooking recipes you have used for years</li></ul></div></li>
    <li class="sign"><span class="sign-num">03</span><div class="sign-text"><span class="sign-head">Get confused about the time, date, or where you are.</span></div></li>
    <li class="sign"><span class="sign-num">04</span><div class="sign-text"><span class="sign-head">Daily tasks are getting harder, including:</span><ul><li>Driving</li><li>Making a grocery list or going shopping</li></ul></div></li>
    <li class="sign"><span class="sign-num">05</span><div class="sign-text"><span class="sign-head">Trouble with how your eyesight and thinking work together that gets worse.</span> <span class="sign-lead">This includes:</span><ul><li>Tripping, falls, or problems with your balance</li><li>Spilling or dropping things more</li></ul></div></li>
    <li class="sign"><span class="sign-num">06</span><div class="sign-text"><span class="sign-head">New trouble talking or writing.</span><br>You may have a harder time finding the words you want to say. For example, you may say “that thing on your wrist that tells time” instead of “watch.”</div></li>
    <li class="sign"><span class="sign-num">07</span><div class="sign-text"><span class="sign-head">Lose and cannot find things.</span> <span class="sign-lead">For example, you:</span><ul><li>Can't find the coffee pot that you use every day</li><li>Might put your car keys in the freezer</li></ul></div></li>
    <li class="sign"><span class="sign-num">08</span><div class="sign-text"><span class="sign-head">Notice changes in mood or personality,</span> <span class="sign-lead">such as being:</span><ul><li>Easily mad or sad in everyday situations</li><li>More fearful (scared) or suspicious (not trusting)</li></ul></div></li>
    <li class="sign"><span class="sign-num">09</span><div class="sign-text"><span class="sign-head">Act different and make poor choices.</span> <span class="sign-lead">You may:</span><ul><li>Spend money you do not have or be a scam victim</li><li>Stop washing up regularly or pay less attention to how you look</li><li>Forget to take care of your pet</li></ul></div></li>
    <li class="sign"><span class="sign-num">10</span><div class="sign-text"><span class="sign-head">Pull away from friends and family because it is harder to keep up.</span><br>You may not want to do things you used to enjoy, like sporting events, church, music, or sex.</div></li>
  </ol>
  <aside class="facts">
    <div class="fact"><div class="fact-icon"><svg width="46" height="46" viewBox="0 0 46 46" fill="none" stroke="#fff" stroke-width="2"><path d="M23 6c-6 0-10 4-10 9s4 8 10 8 10-3 10-8-4-9-10-9z"/><path d="M23 6v17M16 12h4M26 16h4"/><path d="M6 22l6 14h8M40 22l-6 14h-8"/></svg></div><div class="fact-text">American Indian and Alaska Native people have a high risk of dementia.</div></div>
    <div class="fact"><div class="fact-icon"><svg width="46" height="46" viewBox="0 0 46 46" fill="none" stroke="#fff" stroke-width="2"><circle cx="20" cy="9" r="4"/><path d="M20 14v14l-4 12M20 28l5 12M14 20l6-4 6 6"/><path d="M32 22v18"/></svg></div><div class="fact-text">Big changes in memory or thinking that make it hard to get through the day are not a normal part of aging.</div></div>
    <div class="fact"><div class="fact-icon"><svg width="46" height="46" viewBox="0 0 46 46" fill="none" stroke="#fff" stroke-width="2"><circle cx="23" cy="13" r="7"/><path d="M9 40c0-9 6-14 14-14s14 5 14 14z"/><path d="M17 28v6a3 3 0 006 0"/></svg></div><div class="fact-text">People with one or more of these 10 signs should talk to their doctor to find the cause. It is not always dementia.</div></div>
    <div class="fact"><div class="fact-icon"><svg width="46" height="46" viewBox="0 0 46 46" fill="none" stroke="#fff" stroke-width="2"><rect x="9" y="8" width="24" height="32" rx="2"/><rect x="16" y="5" width="10" height="6"/><path d="M21 15v8M17 19h8M14 28h14M14 33h10"/><circle cx="34" cy="34" r="6"/><path d="M31 34l2 2 4-4"/></svg></div><div class="fact-text">Early dementia diagnosis gives you a chance to get care and plan your future.</div></div>
  </aside>
  <div class="hub"><span class="hub-mark"></span><span class="hub-name">Native Elders Brain Wellness Hub</span></div>
  <div class="visit">
    <div class="visit-bar">To learn more, visit:</div>
    <div class="visit-links"><span class="visit-icon"><svg width="20" height="20" viewBox="0 0 20 20" fill="none" stroke="#fff" stroke-width="1.6"><circle cx="10" cy="10" r="8"/><path d="M2 10h16M10 2c3 3 3 13 0 16M10 2c-3 3-3 13 0 16"/></svg></span><span class="visit-urls"><span>www.elderbrainwellness.org</span><span>www.healthyagingnet.org</span></span></div>
  </div>
  <div class="partner-space"></div>
  <p class="funding">This flyer is supported by a public health grant from a federal agency as part of an award for elder brain health outreach. The contents are those of the authors and do not represent official views of, nor an endorsement by, any agency.</p>
</section>
<p class="version-label" style="top:3800px"><span>Version3</span></p>

</body>
</html>
```